We are needing a bookcover for a reprint of our book "Whispers Beneath the Amber Horizon". It takes a look at the geologic formation found in the great plains. Our original cover was colorful and showed rock layers. Something similar but different and eye catching would be great. a geologic cross section showing various layers or possibly some different rocks/soils. We are really open to suggestions attached is the current book cover with the colored layers and the cover from the 80s.

Target Market(s)

Adult Readers

Industry/Entity Type

Nonprofit retail - science - nature

Requirements
Must have
• Geology or rock layers
Nice to have
• Books title, Geologic cross section
Should not have
• People or animals, no photos prefer sketch

```html
<!DOCTYPE html>
<html lang="en">
<head>
<meta charset="utf-8">
<title>Whispers Beneath the Amber Horizon — Book Cover</title>
<link href="https://fonts.googleapis.com/css2?family=Old+Standard+TT:wght@400;700&family=Arimo:ital@1&display=swap" rel="stylesheet">
<style>
  :root {
    --slate: #454b4f;
    --parchment-top: #e9c99a;
    --parchment-mid: #dcae78;
    --ink: #1f1a14;
    --caption: #f2f2f2;
    --frame: #f7f5ef;
    --sky: #dcbf95;
    --hill: #7f9a58;
    --layer-red: #c8452e;
    --layer-orange: #e08a3a;
    --layer-tan: #c99a6a;
    --layer-yellow: #e8d23c;
    --layer-green: #4f9a4a;
    --layer-blue: #3f6fb0;
    --layer-plum: #6b3a48;
    --layer-soil: #d49358;
    --photo-sky: #8fbfd6;
  }
  html, body {
    margin: 0;
    width: 1200px;
    height: 655px;
    overflow: hidden;
    background: var(--slate);
  }
  .canvas {
    position: relative;
    width: 1200px;
    height: 655px;
  }
  .book-cover {
    position: absolute;
    left: 99px;
    top: 44px;
    width: 436px;
    height: 557px;
    background: linear-gradient(180deg, var(--parchment-top), var(--parchment-mid));
    box-shadow: 6px 8px 18px rgba(0,0,0,0.45);
    overflow: hidden;
  }
  .cover-art {
    position: absolute;
    left: 0;
    top: 139px;
    width: 100%;
    height: 418px;
    background: linear-gradient(180deg,
      var(--sky) 0%, var(--hill) 14%, #b39a6c 22%,
      var(--layer-red) 27%, var(--layer-orange) 33%, var(--layer-red) 44%,
      var(--layer-tan) 50%, var(--layer-yellow) 58%, var(--layer-green) 63%,
      var(--layer-blue) 68%, var(--layer-plum) 74%, #5a2f3a 80%,
      var(--layer-soil) 84%, var(--layer-soil) 100%);
  }
  .cover-title {
    position: absolute;
    top: 36px;
    left: 0;
    width: 100%;
    margin: 0;
    text-align: center;
    font-family: "Old Standard TT", serif;
    font-weight: 700;
    font-size: 33px;
    line-height: 1.08;
    color: var(--ink);
  }
  .cover-subtitle {
    position: absolute;
    top: 120px;
    width: 100%;
    margin: 0;
    text-align: center;
    font-family: "Old Standard TT", serif;
    font-size: 15px;
    color: var(--ink);
  }
  .cover-footer {
    position: absolute;
    top: 506px;
    width: 100%;
    margin: 0;
    text-align: center;
    font-family: "Old Standard TT", serif;
    font-size: 13px;
    line-height: 1.35;
    color: var(--ink);
  }
  .section-sketch {
    position: absolute;
    left: 680px;
    top: 44px;
    width: 390px;
    height: 248px;
    box-shadow: 5px 7px 14px rgba(0,0,0,0.45);
    background: linear-gradient(180deg,
      var(--hill) 0%, #a98e62 16%, var(--layer-orange) 26%, var(--layer-red) 46%,
      var(--layer-tan) 54%, var(--layer-yellow) 62%, var(--layer-green) 68%,
      var(--layer-blue) 74%, var(--layer-plum) 82%, var(--layer-soil) 90%, var(--layer-soil) 100%);
  }
  .sketch-caption {
    position: absolute;
    left: 660px;
    top: 305px;
    width: 430px;
    margin: 0;
    text-align: center;
    font-family: "Arimo", sans-serif;
    font-style: italic;
    font-size: 12.5px;
    line-height: 1.65;
    color: var(--caption);
  }
  .vintage-photo {
    position: absolute;
    left: 714px;
    top: 368px;
    width: 327px;
    height: 228px;
    box-sizing: border-box;
    border: 3px solid var(--frame);
    box-shadow: 5px 7px 14px rgba(0,0,0,0.45);
    background: linear-gradient(180deg,
      var(--photo-sky) 0%, #b9d3df 22%, #8d9a6a 28%,
      var(--layer-orange) 36%, #c9652e 56%, #6a3a30 64%,
      #9a8a5e 70%, #b8a98a 100%);
  }
</style>
</head>
<body>
  <main class="canvas">
    <section class="book-cover">
      <div class="cover-art" role="img" aria-label="Sketched landscape of green plains hills above a cross section of red, orange, yellow, green, blue and plum rock layers over sandy soil"></div>
      <h1 class="cover-title">Whispers Beneath<br>the Amber Horizon</h1>
      <p class="cover-subtitle">A Layered Account</p>
      <p class="cover-footer">The Geologic Formation of<br>the Central Great Plains</p>
    </section>

    <div class="section-sketch" role="img" aria-label="Illustrated geologic cross section with grassy surface over banded orange, red, yellow, green, blue and purple strata"></div>
    <p class="sketch-caption">Above: an early geologic section of the plains,<br>showing how the layers rest upon older deposits</p>

    <div class="vintage-photo" role="img" aria-label="Vintage view of an eroded orange sandstone bluff on the open plains under a blue sky"></div>
  </main>
</body>
</html>
```